Cell Tower company needs website updated

We need a website that does not look like it was designed in the early 1990's. The company fabricates, installs and reinforces communication towers throughout the US, Caribbean, Central and S. America. We are located in Pensacola Florida. Our tower technicians travel to wherever the work is. I have some good pictures taken from towers to use on the site. I want the site to reflect the excitement that the wireless communication industry has. I want to the company to look exciting and attract new employees. The majority of our business is modifying and reinforcing existing cell towers to accept all the new tower top antennas that the increasing wireless mobile world demands.

I have added some sample photos from our business to our ArtFoundry profile.

We are now going through each design to find what is most suitable for our needs. Thank you all for your time in this matter.

Wireless Communication

```html
<!DOCTYPE html>
<html lang="en">
<head>
<meta charset="utf-8">
<title>TowerLine — Towering Above the Rest</title>
<link rel="stylesheet" href="https://fonts.googleapis.com/css2?family=Raleway:wght@200;300;400;500;600;800&display=swap">
<style>
  :root {
    --brand-red: #c7282c;
    --brand-red-dark: #a81f23;
    --nav-black: #141414;
    --ink: #2b2b2b;
    --muted: #555555;
    --footer-bg: #f1f1f1;
    --rule: #d6d6d6;
    --white: #ffffff;
    --sky-deep: #2b3a55;
    --sky-glow: #f2a230;
  }
  * { box-sizing: border-box; margin: 0; padding: 0; }
  html, body { width: 876px; height: 1200px; overflow: hidden; }
  body { position: relative; font-family: "Raleway", sans-serif; color: var(--ink); background: var(--white); }
  a { color: inherit; text-decoration: none; }

  /* Hero */
  .hero { position: absolute; left: 0; top: 0; width: 876px; height: 438px; overflow: hidden; }
  .hero-photo { position: absolute; inset: 0;
    background:
      radial-gradient(ellipse 55% 45% at 70% 62%, #ffd56a 0%, rgba(242,162,48,.85) 35%, rgba(200,90,30,.3) 70%, transparent 100%),
      linear-gradient(180deg, #3a4a66 0%, #6b6a6c 28%, #c98a3c 55%, #9a4b1c 80%, #3a2416 100%); }
  .contact-bar { position: absolute; top: 26px; right: 43px; display: flex; align-items: center; gap: 14px; color: var(--white); font-size: 13px; font-weight: 500; }
  .contact-bar .item { display: flex; align-items: center; gap: 5px; }
  .social-dots { display: flex; gap: 8px; margin-left: 4px; }
  .social-dots span { width: 9px; height: 9px; border-radius: 50%; background: var(--white); }
  .brand-box { position: absolute; left: 43px; top: 61px; width: 180px; height: 51px; background: var(--white);
    display: flex; align-items: center; justify-content: center; gap: 7px; }
  .brand-name { font-size: 21px; font-weight: 600; color: var(--ink); }
  .brand-mark { width: 10px; height: 10px; border-radius: 50%; background: var(--brand-red); }
  .main-nav { position: absolute; left: 386px; top: 61px; height: 42px; display: flex; background: var(--nav-black); }
  .main-nav a { display: flex; align-items: center; padding: 0 16px; color: var(--white); font-size: 11px; font-weight: 500; }
  .main-nav a.active { background: var(--brand-red); padding: 0 17px; }
  .search-btn { position: absolute; left: 794px; top: 61px; width: 40px; height: 42px; background: var(--brand-red); display: flex; align-items: center; justify-content: center; }
  .slide-arrow { position: absolute; top: 219px; width: 35px; height: 46px; background: rgba(10,10,10,.85); display: flex; align-items: center; justify-content: center; }
  .slide-arrow.prev { left: 0; } .slide-arrow.next { right: 0; }
  .hero-title { position: absolute; top: 196px; width: 100%; text-align: center; color: var(--white); font-size: 47px; font-weight: 200; letter-spacing: 1px; }
  .hero-title strong { font-weight: 800; }
  .hero-sub { position: absolute; top: 263px; width: 100%; text-align: center; color: var(--white); font-size: 24px; font-weight: 300; }
  .hero-cta { position: absolute; left: 371px; top: 324px; width: 136px; height: 33px; background: var(--brand-red); color: var(--white);
    font-size: 14px; font-weight: 400; display: flex; align-items: center; justify-content: center; }

  /* What we do */
  .tower-art { position: absolute; left: 96px; top: 539px; width: 184px; height: 250px;
    background: radial-gradient(ellipse at 50% 55%, #e8433f 0%, #c7282c 40%, rgba(199,40,44,.15) 75%, transparent 100%); border-radius: 40% 40% 10% 10%; }
  .timeline { position: absolute; left: 346px; top: 503px; width: 1px; height: 318px; background: var(--rule); }
  .timeline-branch { position: absolute; left: 261px; top: 666px; width: 86px; height: 1px; background: var(--rule); }
  .node { position: absolute; width: 7px; height: 7px; border-radius: 50%; background: var(--brand-red); border: 1px solid #f3c3c4; }
  .services-intro { position: absolute; left: 381px; top: 512px; width: 450px; }
  .services-intro h2 { font-size: 20px; font-weight: 400; color: var(--ink); }
  .services-intro p { margin-top: 10px; font-size: 10.5px; line-height: 1.4; color: var(--muted); }
  .offer { position: absolute; left: 381px; width: 450px; }
  .offer .icon { position: absolute; left: 0; top: 0; }
  .offer h3 { margin-left: 41px; font-size: 12px; font-weight: 600; color: var(--ink); }
  .offer p { margin: 10px 0 0 41px; font-size: 10.5px; line-height: 1.4; color: var(--muted); }

  /* Footer */
  .site-footer { position: absolute; left: 0; top: 875px; width: 876px; height: 242px; background: var(--footer-bg); border-top: 1px solid #e2e2e2; }
  .footer-brand { position: absolute; left: 43px; top: 29px; width: 166px; height: 46px; display: flex; align-items: center; gap: 7px; }
  .footer-about { position: absolute; left: 43px; top: 102px; width: 185px; font-size: 10.5px; line-height: 1.35; color: var(--muted); }
  .footer-social { position: absolute; left: 43px; top: 187px; display: flex; gap: 20px; }
  .footer-social span { width: 10px; height: 10px; border-radius: 50%; background: #9a9a9a; }
  .footer-col { position: absolute; top: 33px; width: 182px; }
  .footer-col h4 { display: flex; align-items: center; gap: 10px; font-size: 13px; font-weight: 400; color: var(--ink); }
  .footer-col h4 b { font-weight: 600; }
  .footer-col h4::after { content: ""; flex: 1; height: 1px; background: var(--rule); }
  .footer-col ul { list-style: none; margin-top: 25px; }
  .footer-col li { height: 28.5px; display: flex; align-items: center; gap: 9px; font-size: 10.5px; color: var(--muted); border-bottom: 1px solid #dedede; }
  .footer-col li:last-child { border-bottom: none; }
  .footer-col li::before { content: ""; width: 6px; height: 6px; border-radius: 50%; background: var(--brand-red); }
  .footer-col p { margin-top: 25px; font-size: 10.5px; line-height: 1.35; color: var(--muted); }
  .footer-btn { position: absolute; left: 651px; top: 157px; width: 67px; height: 22px; background: var(--brand-red); color: var(--white);
    font-size: 10px; display: flex; align-items: center; justify-content: center; }
  .bottom-bar { position: absolute; left: 0; top: 1117px; width: 876px; height: 83px; background: var(--brand-red); }
  .bottom-links { position: absolute; left: 43px; top: 35px; display: flex; gap: 10px; font-size: 11.5px; color: #7a1418; }
  .copyright { position: absolute; right: 43px; top: 35px; font-size: 11.5px; color: var(--white); font-weight: 300; }
  .bottom-emblem { position: absolute; left: 414px; top: -14px; width: 16px; height: 97px; background: var(--brand-red-dark); border: 1px solid #e27b7e; }
</style>
</head>
<body>

<header class="hero">
  <div class="hero-photo" role="img" aria-label="Photograph of a communication tower silhouetted against a golden sunset sky"></div>

  <div class="contact-bar">
    <span class="item">
      <svg width="9" height="9" viewBox="0 0 10 10"><path d="M2 1 L4 1 L4.6 3 L3.5 4 Q4.5 6 6 6.6 L7 5.5 L9 6 L9 8 Q5 9 1 4 Q1 2 2 1Z" fill="#d23a3a"/></svg>
      555 010 2424
    </span>
    <span class="item">
      <svg width="11" height="8" viewBox="0 0 11 8"><rect width="11" height="8" fill="#d23a3a"/><path d="M0 0 L5.5 4.5 L11 0" stroke="#fff" stroke-width="1" fill="none"/></svg>
      info@towerline.example
    </span>
    <span class="social-dots"><span></span><span></span><span></span><span></span></span>
  </div>

  <a class="brand-box" href="#"><span class="brand-mark"></span><span class="brand-name">TowerLine</span></a>

  <nav class="main-nav">
    <a class="active" href="#">Home</a>
    <a href="#">About</a>
    <a href="#">Services</a>
    <a href="#">Fabrication</a>
    <a href="#">Jobs</a>
    <a href="#">Contact</a>
  </nav>
  <a class="search-btn" href="#" aria-label="Search">
    <svg width="13" height="13" viewBox="0 0 13 13"><circle cx="5.5" cy="5.5" r="4" stroke="#fff" stroke-width="2" fill="none"/><path d="M8.5 8.5 L12 12" stroke="#fff" stroke-width="2"/></svg>
  </a>

  <a class="slide-arrow prev" href="#" aria-label="Previous slide"><svg width="8" height="13" viewBox="0 0 8 13"><path d="M7 1 L2 6.5 L7 12" stroke="#fff" stroke-width="2" fill="none"/></svg></a>
  <a class="slide-arrow next" href="#" aria-label="Next slide"><svg width="8" height="13" viewBox="0 0 8 13"><path d="M1 1 L6 6.5 L1 12" stroke="#fff" stroke-width="2" fill="none"/></svg></a>

  <h1 class="hero-title">TOWERING <strong>ABOVE</strong> THE REST</h1>
  <p class="hero-sub">REINFORCING FOR THE FUTURE</p>
  <a class="hero-cta" href="#">READ MORE</a>
</header>

<section class="what-we-do">
  <div class="tower-art" role="img" aria-label="Illustration of a red communication tower emitting orange signal waves"></div>
  <div class="timeline"></div>
  <div class="timeline-branch"></div>
  <span class="node" style="left:343px;top:499px"></span>
  <span class="node" style="left:343px;top:663px"></span>
  <span class="node" style="left:343px;top:817px"></span>

  <div class="services-intro">
    <h2>What We Do</h2>
    <p>TowerLine, Inc., is an experienced and innovative provider of communication towers, tower reinforcements and related support services.</p>
  </div>

  <div class="offer" style="top:594px">
    <svg class="icon" width="24" height="24" viewBox="0 0 24 24"><path d="M17 2 A5 5 0 0 0 12 8 L2 18 L5 21 L15 11 A5 5 0 0 0 22 6 L19 8 L16 6 L18 3Z" fill="var(--brand-red)"/></svg>
    <h3>Services</h3>
    <p>The management team at TowerLine is ready to provide you with 100+ years of experience fabricating.</p>
  </div>
  <div class="offer" style="top:673px">
    <svg class="icon" width="26" height="22" viewBox="0 0 26 22"><rect x="9" y="1" width="8" height="4" fill="none" stroke="var(--brand-red)" stroke-width="2"/><rect x="1" y="5" width="24" height="16" rx="2" fill="var(--brand-red)"/><rect x="1" y="11" width="24" height="1.5" fill="#fff"/></svg>
    <h3>Fabrication</h3>
    <p>The management team at TowerLine is ready to provide you with 100+ years of experience fabricating.</p>
  </div>
  <div class="offer" style="top:752px">
    <svg class="icon" width="27" height="20" viewBox="0 0 27 20"><path d="M1 2 L9 2 L11 4 L22 4 L22 7 L6 7 L1 19Z" fill="var(--brand-red)"/><path d="M6 8 L26 8 L21 19 L1 19Z" fill="var(--brand-red)"/></svg>
    <h3>Jobs</h3>
    <p>The management team at TowerLine is ready to provide you with 100+ years of experience fabricating.</p>
  </div>
</section>

<footer class="site-footer">
  <a class="footer-brand" href="#"><span class="brand-mark"></span><span class="brand-name">TowerLine</span></a>
  <p class="footer-about">Suspendisse condimentum mollis vehicula. Praesent sodales interdum elit interdum ornare. Suspendisse tristique semper arcu nec.</p>
  <div class="footer-social"><span></span><span></span><span></span><span></span></div>

  <div class="footer-col" style="left:245px">
    <h4>Our <b>Site</b></h4>
    <ul><li>Home</li><li>Services</li><li>Fabrication</li><li>Jobs</li><li>Contact</li></ul>
  </div>
  <div class="footer-col" style="left:449px">
    <h4>Our <b>Services</b></h4>
    <ul><li>Monopole Reinforcements</li><li>Tower Reinforcements</li><li>Fabrication</li><li>Install Services</li><li>Reinforcment Drawings</li></ul>
  </div>
  <div class="footer-col" style="left:651px">
    <h4>Work with <b>Us</b></h4>
    <p>Suspendisse condimentum mollis vehicula. Praesent sodales interdum elit interdum ornare. Suspendisse tristique semper arcu nec.</p>
  </div>
  <a class="footer-btn" href="#">Read more</a>
</footer>

<div class="bottom-bar">
  <div class="bottom-emblem" role="img" aria-label="Small line drawing of a signal tower"></div>
  <nav class="bottom-links"><a href="#">About Us</a><a href="#">Blog</a><a href="#">Contact Us</a></nav>
  <p class="copyright">© Copyright 2014 TowerLine Inc.</p>
</div>

</body>
</html>
```